Support Welcome Packet Redesign

Looking to redesign our current "welcome packet" that we send to our new customers to help them understand our support service. It is currently in Microsoft Word and would like to remain in either word or publisher. Something that we can easily edit, as the content adjusts based on the customer needs. We want this document to be simple and understandable as it should be something our customers can reference at any time during our contract and easy to navigate.

Target Market(s)

Current Customers. Healthcare, Oil & Gas, Transportation, etc.

Industry/Entity Type

It Service

Font styles to use
Sans Serif

Requirements
Must have
• Table of Contents, exWave Logo and current content
Nice to have
• Easy navigation. Redone final page (contact info)

```html
<!DOCTYPE html>
<html lang="en">
<head>
<meta charset="utf-8">
<title>exWave Support Welcome Packet</title>
<link href="https://fonts.googleapis.com/css2?family=PT+Sans:wght@400;700&family=PT+Sans+Narrow:wght@700&display=swap" rel="stylesheet">
<style>
  :root {
    --page: #ffffff;
    --navy: #2f5489;
    --navy-text: #1f4c86;
    --row-a: #a6bcdc;
    --row-b: #d0ddee;
    --num: #4a4f57;
    --amber: #fdbb00;
    --sky: #3399ff;
    --line: #5a86b8;
    --teal: #6fa3b8;
    --orange: #f07c1e;
    --frame: #7a7a7a;
  }
  * { margin: 0; padding: 0; box-sizing: border-box; }
  html, body { width: 927px; height: 1200px; overflow: hidden; background: var(--page); }
  .page { position: relative; width: 927px; height: 1200px; font-family: "PT Sans", sans-serif; }
  .frame-lines { position: absolute; inset: 0; }
  .panel { position: absolute; }
  .panel--amber { left: 36px; top: 258px; width: 411px; height: 901px; background: var(--amber); border-radius: 44px 44px 40px 44px; }
  .panel--sky { left: 462px; top: 159px; width: 432px; height: 1000px; background: var(--sky); border-radius: 36px; }
  .brand { position: absolute; left: 80px; top: 52px; width: 150px; text-align: center; }
  .brand__mark { width: 70px; height: 70px; margin: 0 auto 14px; background: var(--orange); border-radius: 10px; }
  .brand__name { font-size: 36px; font-weight: 400; color: var(--orange); line-height: 1; }
  .brand__tag { font-size: 10px; color: #333; margin-top: 4px; }
  .welcome { position: absolute; left: 500px; top: 53px; width: 394px; height: 84px;
    background: linear-gradient(90deg, rgba(255,255,255,1) 0%, #c9d8ee 55%, #9bb6dd 100%);
    display: flex; align-items: center; justify-content: flex-end; padding-right: 30px; }
  .welcome__title { font-size: 62px; font-weight: 700; color: var(--navy-text); letter-spacing: 0.5px; }
  .toc { position: absolute; left: 64px; top: 321px; width: 784px; border: 2px solid #fff; background: #fff; }
  .toc__head { height: 68px; background: var(--navy); color: #fff; font-size: 42px; font-weight: 700;
    display: flex; align-items: center; justify-content: center; font-family: "PT Sans Narrow", "PT Sans", sans-serif; }
  .toc__row { display: flex; height: 51.5px; border-top: 2px solid #fff; }
  .toc__label { width: 390px; background: var(--navy); color: #fff; font-weight: 700; font-size: 20px;
    display: flex; align-items: center; font-family: "PT Sans Narrow", "PT Sans", sans-serif; }
  .toc__page { flex: 1; display: flex; align-items: center; justify-content: flex-end; padding-right: 12px;
    font-size: 29px; font-weight: 700; color: var(--num); }
  .toc__row:nth-child(odd) .toc__page { background: var(--row-a); }
  .toc__row:nth-child(even) .toc__page { background: var(--row-b); }
  .lvl-1 { padding-left: 9px; }
  .lvl-2 { padding-left: 21px; }
  .lvl-3 { padding-left: 33px; }
  .support-art { position: absolute; left: 630px; top: 965px; width: 262px; height: 175px;
    background: radial-gradient(ellipse at 55% 45%, #1f5fa8 0%, #2e7fd6 45%, rgba(51,153,255,0) 75%); border-radius: 20px; }
</style>
</head>
<body>
<div class="page">
  <div class="panel panel--amber"></div>
  <div class="panel panel--sky"></div>

  <svg class="frame-lines" width="927" height="1200" viewBox="0 0 927 1200" aria-hidden="true">
    <path d="M36 30 H500" stroke="var(--frame)" stroke-width="1.5" stroke-dasharray="3 3" fill="none"/>
    <path d="M36 30 V1164 H921 V640" stroke="var(--frame)" stroke-width="1.5" stroke-dasharray="3 3" fill="none"/>
    <path d="M451 262 V190 Q451 150 491 150 H927" stroke="var(--line)" stroke-width="3" fill="none"/>
    <path d="M36 244 H420 Q470 244 470 294 V420" stroke="var(--teal)" stroke-width="2.5" fill="none"/>
    <path d="M467 860 V1168" stroke="#1e3f78" stroke-width="3" fill="none"/>
    <path d="M450 1168 L927 840" stroke="#d8ecff" stroke-width="1.5" fill="none"/>
    <path d="M520 1168 L927 880" stroke="#d8ecff" stroke-width="1" fill="none"/>
    <path d="M860 706 H927" stroke="#c9d3de" stroke-width="1.5" fill="none"/>
  </svg>

  <div class="brand">
    <div class="brand__mark"></div>
    <div class="brand__name">exWave</div>
    <div class="brand__tag">Technology Corp.</div>
  </div>

  <div class="welcome"><h1 class="welcome__title">Welcome</h1></div>

  <nav class="toc">
    <div class="toc__head">Table of Contents</div>
    <div class="toc__body">
      <div class="toc__row"><div class="toc__label lvl-1">Document Summary</div><div class="toc__page">2</div></div>
      <div class="toc__row"><div class="toc__label lvl-1">Services Summary</div><div class="toc__page">3</div></div>
      <div class="toc__row"><div class="toc__label lvl-1">Support Information</div><div class="toc__page">4</div></div>
      <div class="toc__row"><div class="toc__label lvl-2">exWave Support Teams and Escalation Path</div><div class="toc__page">4 to 5</div></div>
      <div class="toc__row"><div class="toc__label lvl-2">exWave Support Escalation Matrix</div><div class="toc__page">6</div></div>
      <div class="toc__row"><div class="toc__label lvl-3">Priority Level</div><div class="toc__page">6 to 7</div></div>
      <div class="toc__row"><div class="toc__label lvl-3">Escalation Guidelines</div><div class="toc__page">8 to 9</div></div>
      <div class="toc__row"><div class="toc__label lvl-2">exWave Support Contact Information</div><div class="toc__page">10</div></div>
      <div class="toc__row"><div class="toc__label lvl-2">exWave Support</div><div class="toc__page">11</div></div>
    </div>
  </nav>

  <div class="support-art" role="img" aria-label="Illustration of a desktop computer with keyboard and mouse surrounded by colourful swirling arrows"></div>
</div>
</body>
</html>
```